Accident Law Firm Billboard Bold Easy to See Car Accidents

We need a billboard design that can catch attention in a very crowed Car Accident lawyer market. We wish to feature the phone number (652) 318-4470 as the focus of the Bill Board. We are trying to get the phone number recognized and remembered by drivers. The law firm name is not as crucial to remember.
Basically, It's CAR ACCIDENT? Then (652) 318-4470. We are not married to any specific color scheme but it has to POP and catch attention.
So the Crucial elements are as follows:
1. Phone number (652) 318-4470
2. Words CAR ACCIDENT?
3. Firm Logo in lower portion or where appropriate. Firm Logo to be provided
4. We may want to try a Day Glow orange color, with White and Black added. An example of the color scheme shall be provided.
5. Possible "Catch Phrase" to be used, "It's Time Call 9"
Target Market(s)
Orlando Florida Car Accident victims
Industry/Entity Type
Law Firm
Requirements
Must have
- Easy to see phone number (652) 318-4470
- Catch attention
Nice to have
- I would like to have the sign visible in bright sunlight and it not too hard to immediately know what phone number is for
Should not have
- too many words
- No bold enough
- confusing fonts
- Unclear fonts

```html
<!DOCTYPE html>
<html lang="en">
<head>
<meta charset="UTF-8">
<title>Car Accident Billboard – Marlowe Law Firm P.C.</title>
<link href="https://fonts.googleapis.com/css2?family=Alfa+Slab+One&display=swap" rel="stylesheet">
<style>
  :root {
    --page-bg: #eef1f3;
    --dayglow-orange: #ef6a1f;
    --dayglow-orange-deep: #e2561a;
    --dayglow-orange-light: #f47d2c;
    --ink-white: #ffffff;
  }
  html, body {
    margin: 0;
    padding: 0;
    width: 1200px;
    height: 794px;
    overflow: hidden;
    background: var(--page-bg);
  }
  .canvas {
    position: relative;
    width: 1200px;
    height: 794px;
  }
  .billboard {
    position: absolute;
    left: 0;
    top: 213px;
    width: 1200px;
    height: 367px;
    background: linear-gradient(160deg, var(--dayglow-orange-deep) 0%, var(--dayglow-orange) 45%, var(--dayglow-orange-light) 100%);
    color: var(--ink-white);
    font-family: "Alfa Slab One", "Rockwell", serif;
    overflow: hidden;
  }
  .headline,
  .phone-line,
  .tagline {
    position: absolute;
    margin: 0;
    white-space: nowrap;
    line-height: 1;
    font-weight: 400;
  }
  .headline {
    left: 146px;
    top: 52px;
    font-size: 70px;
    letter-spacing: 1px;
  }
  .phone-line {
    left: 178px;
    top: 160px;
    font-size: 66px;
    letter-spacing: 1px;
  }
  .tagline {
    left: 176px;
    top: 246px;
    font-size: 29px;
    letter-spacing: 0;
  }
  .firm-name {
    position: absolute;
    left: 978px;
    top: 300px;
    width: 180px;
    color: var(--ink-white);
    font-family: "Alfa Slab One", "Rockwell", serif;
    text-align: left;
    line-height: 1.05;
  }
  .firm-name__main {
    display: block;
    font-size: 23px;
    letter-spacing: 1px;
  }
  .firm-name__sub {
    display: block;
    font-size: 12px;
    letter-spacing: 3px;
  }
</style>
</head>
<body>
  <main class="canvas">
    <section class="billboard" aria-label="Car accident law firm billboard">
      <h1 class="headline">It's CAR ACCIDENT?</h1>
      <p class="phone-line">Then (652) 318-4470</p>
      <p class="tagline">CALL YOUR NEXT WITNESS</p>
      <div class="firm-name">
        <span class="firm-name__main">MARLOWE</span>
        <span class="firm-name__sub">LAW FIRM P.C.</span>
      </div>
    </section>
  </main>
</body>
</html>
```